Business Card Design for Mabel's Larder

We make food for dogs.
Business Card Design (using the logo designed by you). Our Brand color is a bright canary yellow. For example our signage is predominantly yellow, with the logo in black. I'd like the card also to use that imagery.
Feel free to use the two sides creatively.
Vertical Design is also great.

Industry/Entity Type

Pet food

Contact Information for Business Card

Name, email, website, phone no

Font styles to use
Sans Serif

Colors
59FF00
82FF00
B8FF75
E3FFCB
F4FFEA
FFF300
FFF600
FEFA6F
FFFEC7
FFFEE8

Requirements
Nice to have
• A graphic in the same brush stroke style of the logo shoeing a doggy bowl of food

```html
<!DOCTYPE html>
<html lang="en">
<head>
<meta charset="utf-8">
<title>Mabel's Larder — Business Card</title>
<link rel="stylesheet" href="https://fonts.googleapis.com/css2?family=Oswald:wght@500&family=Kalam:wght@400&family=Lora:wght@400&display=swap">
<style>
  :root {
    --page-bg: #eeebec;
    --canary: #fce44f;
    --ink: #111111;
    --card-white: #ffffff;
    --muted-ink: #333333;
    --kibble-light: #efe8df;
    --kibble-mid: #cdb79c;
    --kibble-dark: #a88a68;
  }
  * { box-sizing: border-box; margin: 0; padding: 0; }
  html, body {
    width: 1200px;
    height: 1200px;
    overflow: hidden;
    background: var(--page-bg);
  }
  .sheet {
    position: relative;
    width: 1200px;
    height: 1200px;
  }
  .card {
    position: absolute;
    left: 240px;
    width: 720px;
    height: 410px;
    border-radius: 36px;
    overflow: hidden;
    box-shadow: 0 18px 40px rgba(0, 0, 0, 0.18);
  }
  .card--front {
    top: 130px;
    background: var(--canary);
    display: flex;
    align-items: center;
    justify-content: center;
  }
  .brand-name {
    font-family: "Oswald", sans-serif;
    font-weight: 500;
    font-size: 66px;
    letter-spacing: 1px;
    color: var(--ink);
    text-transform: uppercase;
    white-space: nowrap;
  }
  .card--back {
    top: 660px;
    background: var(--card-white);
  }
  .kibble-photo {
    position: absolute;
    top: 0;
    right: 0;
    width: 470px;
    height: 100%;
    background:
      radial-gradient(ellipse 160px 90px at 320px 90px, rgba(168,138,104,0.55), transparent 70%),
      radial-gradient(ellipse 190px 110px at 330px 300px, rgba(168,138,104,0.6), transparent 70%),
      radial-gradient(ellipse 140px 80px at 150px 260px, rgba(205,183,156,0.45), transparent 70%),
      linear-gradient(90deg, var(--card-white) 0%, var(--kibble-light) 45%, var(--kibble-light) 100%);
    opacity: 0.75;
  }
  .back-content {
    position: absolute;
    inset: 0;
    display: flex;
    align-items: center;
    padding-left: 80px;
  }
  .person {
    text-align: right;
    padding-right: 26px;
    white-space: nowrap;
  }
  .person__name {
    font-family: "Kalam", cursive;
    font-size: 40px;
    letter-spacing: 2px;
    color: var(--ink);
    line-height: 1.1;
  }
  .person__role {
    font-family: "Lora", serif;
    font-size: 18px;
    color: var(--muted-ink);
  }
  .divider {
    width: 2px;
    height: 120px;
    background: var(--muted-ink);
    flex: none;
  }
  .contact-list {
    list-style: none;
    padding-left: 24px;
    font-family: "Lora", serif;
    font-size: 19px;
    color: var(--muted-ink);
    line-height: 1.75;
  }
  .contact-list__item {
    display: flex;
    white-space: nowrap;
  }
  .contact-list__label {
    flex: none;
    width: 38px;
    white-space: nowrap;
  }
</style>
</head>
<body>
  <main class="sheet">
    <section class="card card--front" aria-label="Card front">
      <h1 class="brand-name">Mabel's Larder</h1>
    </section>

    <section class="card card--back" aria-label="Card back">
      <div class="kibble-photo" role="img" aria-label="Soft-focus photo of a white bowl and scoop of dry dog kibble"></div>
      <div class="back-content">
        <div class="person">
          <p class="person__name">PETER HALE</p>
          <p class="person__role">Founder</p>
        </div>
        <div class="divider"></div>
        <ul class="contact-list">
          <li class="contact-list__item"><span class="contact-list__label">T .</span>000.555.014.2020</li>
          <li class="contact-list__item"><span class="contact-list__label">W .</span>mabelslarder.Com</li>
          <li class="contact-list__item"><span class="contact-list__label">E .</span>peter@mabelslarder.Com</li>
        </ul>
      </div>
    </section>
  </main>
</body>
</html>
```